Home Page and One Inside Page Needed for Engine Modify Site

Website that sells kits to modify and enhance your car engine performance. I don't like direction / design of current site at http://www.vortalmotorhaus.com.php61-24.sto3-2.pagedraftzone.com/

I want something modern. Something that shows power and performance.

I need home page and one inside page.

Keep blues and blacks and unfortunately that is their logo we have to work with. But this site needs WOW factor.

YOU DO NOT HAVE PERMISSION TO WORK OR SPEAK TO CLIENT DIRECTLY AND MUST WORK THROUGH ME.

```html
<!DOCTYPE html>
<html lang="en">
<head>
<meta charset="utf-8">
<title>vortalmotorhaus – precision exhaust header modeling system</title>
<link rel="stylesheet" href="https://fonts.googleapis.com/css2?family=Arimo:wght@400;700&family=Open+Sans:wght@400;600;700&display=swap">
<style>
:root{
  --blue:#0a0aff;
  --blue-text:#1414e6;
  --sky:#4a7fa8;
  --black:#000;
  --dark:#333333;
  --ink:#1c2330;
  --grey:#7a7a7a;
  --light:#f4f4f4;
  --line:#dcdcdc;
  --white:#fff;
}
*{box-sizing:border-box;margin:0;padding:0}
html,body{width:933px;height:1200px;overflow:hidden}
body{position:relative;background:var(--light);font-family:"Open Sans",sans-serif;color:var(--grey)}
.abs{position:absolute}
a{color:inherit;text-decoration:none}

/* header */
.header{left:0;top:0;width:933px;height:54px;background:var(--white)}
.nav-band{left:0;top:0;width:933px;height:62px}
.brand{left:146px;top:6px}
.brand-name{font-family:"Arimo",sans-serif;font-weight:700;font-size:24px;color:var(--blue-text);line-height:1;letter-spacing:.2px}
.brand-tag{font-family:"Arimo",sans-serif;font-size:8px;color:#222;margin-top:2px}
.nav{left:382px;top:18px;display:flex;align-items:center;font-size:10.5px;color:var(--white)}
.nav a{padding:0 11px;height:18px;line-height:18px;position:relative}
.nav a.active{background:var(--blue);padding:0 13px;clip-path:polygon(4px 0,100% 0,100% 100%,0 100%)}
.nav .sep{color:#777;font-size:11px}

/* hero */
.hero{left:0;top:54px;width:933px;height:358px;background:linear-gradient(135deg,#6b6b6b 0%,#9a9a9a 35%,#5c5c5c 60%,#8d8d8d 100%)}
.slider{left:146px;top:94px;width:639px;height:298px;background:radial-gradient(ellipse at 70% 45%,#1010a0 0%,#07075a 45%,#050525 100%);border:1px solid #555}
.slide-tab{left:160px;top:134px;width:194px;height:30px;background:var(--blue);clip-path:polygon(0 0,88% 0,100% 100%,0 100%);color:var(--white);font-family:"Arimo",sans-serif;font-weight:700;font-size:14.5px;line-height:30px;padding-left:12px}
.slide-list{left:165px;top:187px;list-style:none;font-size:8.3px;color:#d8d8e8;line-height:16.8px}
.slide-list li::before{content:":: ";}
.btn-grey{left:167px;top:271px;width:95px;height:27px;background:#666;clip-path:polygon(0 0,82% 0,100% 100%,0 100%);color:var(--white);font-size:10px;line-height:27px;padding-left:13px}
.product-shot{left:472px;top:148px;width:252px;height:160px;background:radial-gradient(ellipse,#cfd3dc 0%,#8a90a6 45%,rgba(20,20,120,0) 75%)}
.dots{left:692px;top:362px;display:flex;gap:5px}
.dots span{width:9px;height:9px;background:var(--white)}
.dots span.on{background:#8f95ff}
.welcome{left:146px;top:374px;width:336px;height:38px;background:var(--white);clip-path:polygon(0 0,89% 0,100% 100%,0 100%);font-family:"Arimo",sans-serif;font-size:16px;line-height:44px;padding-left:17px;color:var(--sky);white-space:nowrap}
.welcome b{color:var(--ink)}

/* intro */
.intro{left:0;top:412px;width:933px;height:146px;background:var(--white);border-bottom:1px solid var(--line)}
.intro p{position:absolute;left:160px;top:10px;width:614px;font-size:8.3px;line-height:13.6px;color:var(--grey)}
.btn-blue{left:162px;top:493px;width:83px;height:27px;background:var(--blue);clip-path:polygon(0 0,85% 0,100% 100%,0 100%);color:var(--white);font-size:9.5px;line-height:27px;padding-left:13px}

/* how it works */
.section-badge{left:413px;top:542px;width:163px;height:32px;background:#e6e6e6;clip-path:polygon(6% 0,94% 0,100% 50%,94% 100%,6% 100%,0 50%);font-family:"Arimo",sans-serif;font-weight:700;font-size:17.5px;color:var(--ink);text-align:center;line-height:33px}
.step{top:603px;height:75px;background:var(--dark);color:var(--white)}
.step-one{left:146px;width:333px;clip-path:polygon(0 0,88% 0,100% 100%,0 100%)}
.step-two{left:454px;width:332px;clip-path:polygon(0 0,100% 0,100% 100%,12% 100%)}
.step-num{top:7px;width:38px;height:38px;background:var(--white);color:var(--ink);font-family:"Arimo",sans-serif;font-weight:700;font-size:24px;text-align:center;line-height:38px}
.step-title{top:6px;font-size:11.5px}
.step-text{top:25px;font-size:7.8px;line-height:12px;color:#eee}
.step-more{top:54px;height:21px;width:76px;background:var(--white);color:var(--ink);font-size:8px;line-height:21px;padding-left:16px;clip-path:polygon(0 0,86% 0,100% 100%,14% 100%)}
.divider{left:146px;top:708px;width:640px;height:1px;background:var(--line)}

/* columns */
.h3{font-family:"Arimo",sans-serif;font-weight:700;font-size:16px;color:var(--ink)}
.cats{left:151px;top:752px;list-style:none;font-size:8px;line-height:16.6px}
.cats li::before{content:"→";margin-right:6px;color:#555;font-size:7px}
.cats li.current{color:var(--blue-text)}
.frame{border:1px solid #ccc;background:var(--white);padding:4px}
.photo{width:100%;height:100%}
.who-title{left:534px;top:752px;font-size:11.5px;color:var(--blue-text)}
.who-text{left:534px;top:771px;width:252px;font-size:7.9px;line-height:12px}
.btn-dark{left:696px;top:831px;width:90px;height:25px;background:var(--dark);clip-path:polygon(12% 0,100% 0,100% 100%,0 100%);color:var(--white);font-size:8.8px;line-height:25px;text-align:right;padding-right:22px}
.news-box{left:146px;top:893px;width:166px;height:64px;background:var(--white);border:1px solid #e2e2e2;padding:8px 9px;font-size:7.9px;line-height:12px;color:#333}
.news-date{left:147px;top:966px;width:74px;height:21px;background:var(--dark);clip-path:polygon(0 0,82% 0,100% 100%,0 100%);color:var(--white);font-size:9px;line-height:21px;padding-left:6px}
.thumb{top:893px;width:128px;height:94px}

/* footer */
.footer{left:0;top:1014px;width:933px;height:140px;background:var(--dark)}
.ft-title{top:1025px;font-size:12px;color:var(--white)}
.ft-nav{left:146px;top:1045px;list-style:none;font-size:8.5px;line-height:16.6px;color:#777}
.ft-nav li::before{content:"→";margin-right:6px;font-size:7px}
.ft-nav li.current{color:var(--white)}
.social{left:314px;width:94px;height:22px;background:#f0f0f0;clip-path:polygon(0 0,86% 0,100% 100%,0 100%);font-size:8.5px;color:#333;line-height:22px;padding-left:30px}
.social i{position:absolute;left:5px;top:3px;width:16px;height:16px;background:#333}
.contact{left:465px;top:1047px;font-size:8.2px;line-height:13.4px;color:#999;font-style:normal}
.field{left:615px;top:1050px;width:171px;height:20px;background:#2a2a2a;border:1px solid #444;font-size:8px;color:#666;line-height:18px;padding-left:6px}
.btn-sub{left:615px;top:1076px;width:71px;height:18px;background:#eee;clip-path:polygon(0 0,82% 0,100% 100%,0 100%);color:#111;font-size:9px;line-height:18px;padding-left:10px}
.copyright{left:0;top:1167px;width:933px;text-align:center;font-size:8px;color:#333}
</style>
</head>
<body>

<!-- header -->
<div class="abs header"></div>
<svg class="abs nav-band" width="933" height="62" viewBox="0 0 933 62">
  <polygon points="352,0 933,0 933,54 374,60" fill="#000"/>
</svg>
<div class="abs brand">
  <div class="brand-name">vortalmotorhaus</div>
  <div class="brand-tag">precision exhaust header modeling system</div>
</div>
<nav class="abs nav">
  <a class="active" href="#">Home</a>
  <a href="#">About Us</a><span class="sep">\</span>
  <a href="#">Product</a><span class="sep">\</span>
  <a href="#">Resources</a><span class="sep">\</span>
  <a href="#">How It Works</a><span class="sep">\</span>
  <a href="#">Contact Us</a>
</nav>

<!-- hero -->
<div class="abs hero" role="img" aria-label="Engine bay with exhaust manifold, dark grey photograph"></div>
<div class="abs slider"></div>
<div class="abs slide-tab">IMAGINE NO MORE</div>
<ul class="abs slide-list">
  <li>Imagine designing precise exhaust header full-scale 3D.....</li>
  <li>Imagine being able to do it in a matter of hours instead...</li>
  <li>Imagine making unlimited corrections without....</li>
  <li>Imaginedetermining how much metal you will need...</li>
</ul>
<a class="abs btn-grey" href="#">READ MORE</a>
<div class="abs product-shot" role="img" aria-label="Chrome exhaust header product"></div>
<svg class="abs" style="left:664px;top:352px" width="24" height="30" viewBox="0 0 24 30"><polyline points="16,2 3,15 16,28" fill="none" stroke="#bbb" stroke-width="1.2"/></svg>
<div class="abs dots"><span class="on"></span><span></span><span></span><span></span></div>
<svg class="abs" style="left:754px;top:352px" width="24" height="30" viewBox="0 0 24 30"><polyline points="6,2 19,15 6,28" fill="none" stroke="#bbb" stroke-width="1.2"/></svg>
<div class="abs welcome">welcome to <b>VORTALMOTORHAUS</b></div>

<!-- intro -->
<section class="abs intro">
  <p>Lorem Ipsum is simply dummy text of the printing and typesetting industry. Lorem Ipsum has been the industry's standard dummy text ever since the 1500s, when an unknown printer took a galley of type and scrambled it to make a type specimen book. It has survived not only five centuries, but also the leap into electronic typesetting, remaining essentially unchanged. It was popularised in the 1960s with the release of Letterline sheets containing Lorem Ipsum passages, and more recently with desktop publishing software like Folio Layout including versions of Lorem Ipsum....</p>
</section>
<a class="abs btn-blue" href="#">READ MORE</a>

<!-- how it works -->
<div class="abs section-badge">HOW IT WORKS</div>
<div class="abs step step-one">
  <div class="abs step-num" style="left:6px">1</div>
  <div class="abs step-title" style="left:60px">Design &amp; Modeling</div>
  <div class="abs step-text" style="left:60px;width:230px">Regardless of the engine type, exhaust and engine builders are presented with a very challenging problem...</div>
  <a class="abs step-more" style="left:218px" href="#">READ MORE</a>
</div>
<div class="abs step step-two">
  <div class="abs step-num" style="left:288px">2</div>
  <div class="abs step-title" style="right:56px">Fabrcation &amp; Welding</div>
  <div class="abs step-text" style="right:56px;width:240px;text-align:right">J- or U-bends are all it takes to turn designs modeled with pl -astic blocks into a full metal version thanks to the ....</div>
  <a class="abs step-more" style="left:66px" href="#">READ MORE</a>
  <div class="abs" style="left:209px;top:54px;font-size:8px;line-height:21px">READ MORE</div>
</div>
<div class="abs divider"></div>
<svg class="abs" style="left:460px;top:702px" width="14" height="14" viewBox="0 0 14 14"><g fill="#ddd"><rect x="5" y="0" width="4" height="4"/><rect x="0" y="5" width="4" height="4"/><rect x="10" y="5" width="4" height="4"/><rect x="5" y="10" width="4" height="4"/></g></svg>

<!-- categories -->
<div class="abs h3" style="left:147px;top:726px">Categories</div>
<ul class="abs cats">
  <li class="current">1625 Series Products</li>
  <li>1750 Series Products</li>
  <li>2000 Series Products</li>
  <li>Fabrication Tools</li>
  <li>Pre-Bent Tubing</li>
  <li>Other Products</li>
</ul>

<!-- who is using it -->
<div class="abs h3" style="left:333px;top:723px">Who is Using It?</div>
<div class="abs frame" style="left:334px;top:752px;width:183px;height:90px">
  <div class="photo" role="img" aria-label="Workshop fitting orange header tubes to an engine" style="background:linear-gradient(135deg,#3a3a3a,#c9652a 45%,#2c2c2c)"></div>
</div>
<a class="abs who-title" href="#">Neque porro quisquam est qui dolorem ipsum</a>
<p class="abs who-text">Lorem Ipsum is simply dummy text of the printing and typesetting industry. Lorem Ipsum has been the industry's standard dummy text ever since the 1500s, when an unknown printer took a galley of type and scrambled it to make a type specimen book . . .</p>
<a class="abs btn-dark" href="#">VIEW ALL</a>
<div class="abs" style="left:333px;top:856px;width:453px;height:1px;background:var(--line)"></div>

<!-- latest news -->
<div class="abs h3" style="left:146px;top:866px">Latest News</div>
<svg class="abs" style="left:286px;top:868px" width="24" height="12" viewBox="0 0 24 12"><polyline points="6,1 1,6 6,11" fill="none" stroke="#222" stroke-width="1.6"/><polyline points="18,1 23,6 18,11" fill="none" stroke="#222" stroke-width="1.6"/></svg>
<div class="abs news-box">Lorem Ipsum is simply dummy text of the printing and typesetting industry. Lorem Ipsum has been the industry's standard dummy..</div>
<div class="abs news-date">17 July 2013</div>

<!-- gallery -->
<div class="abs h3" style="left:333px;top:866px">View Our Gallery</div>
<svg class="abs" style="left:332px;top:920px" width="16" height="28" viewBox="0 0 16 28"><polyline points="13,1 2,14 13,27" fill="none" stroke="#555" stroke-width="1.2"/></svg>
<div class="abs frame thumb" style="left:354px"><div class="photo" role="img" aria-label="Engine bay with blue intake" style="background:linear-gradient(135deg,#4a5260,#2a4a8a 50%,#bfc3c8)"></div></div>
<div class="abs frame thumb" style="left:494px"><div class="photo" role="img" aria-label="Engine with chrome headers" style="background:linear-gradient(135deg,#bbb,#555 50%,#2a2a2a)"></div></div>
<div class="abs frame thumb" style="left:634px"><div class="photo" role="img" aria-label="Mechanic working on an engine" style="background:linear-gradient(135deg,#222,#8a7a5a 50%,#d8d8d8)"></div></div>
<svg class="abs" style="left:770px;top:920px" width="16" height="28" viewBox="0 0 16 28"><polyline points="3,1 14,14 3,27" fill="none" stroke="#555" stroke-width="1.2"/></svg>

<!-- footer -->
<footer class="abs footer"></footer>
<div class="abs ft-title" style="left:146px">Navigation</div>
<ul class="abs ft-nav">
  <li class="current">Home</li>
  <li>About Us</li>
  <li>Product</li>
  <li>Resources</li>
  <li>How It Works</li>
  <li>Contact Us</li>
</ul>
<div class="abs ft-title" style="left:310px">Connect with Us</div>
<a class="abs social" style="top:1048px" href="#"><i></i>Circlebook</a>
<a class="abs social" style="top:1077px" href="#"><i></i>Chirper</a>
<a class="abs social" style="top:1106px" href="#"><i></i>ClipStream</a>
<div class="abs ft-title" style="left:464px">Contact Address</div>
<address class="abs contact">
  48 Larkfield Road Denton,<br>TX 76201<br>Phone: (555) 014 2232<br>Fax: (555) 014 2282<br>M-F 9-6<br>Email: info@vortalmotorhaus.com
</address>
<div class="abs ft-title" style="left:615px">Subscribe for News Letter</div>
<div class="abs field">Your E-mail ID</div>
<a class="abs btn-sub" href="#">Subscribe</a>
<div class="abs copyright">2013 © Vortalmotorhaus. All rights Reserved.</div>

</body>
</html>
```